Business Card Design - Crisp & Clean

Looking for a new clean and crisp business card design. Design must incorporate our corporate colors (see attached style sheet). We're a pretty fun loving group who likes to keep it light while still portraying a professional image. Card should incorporate both our logo and our mascot (see attachment). Card should be double sided and should have room for our social media - Gleamrow, Brisk Hub and Zumbly on the back. Font selections do not have to match the style guide.

```html
<!DOCTYPE html>
<html lang="en">
<head>
<meta charset="utf-8">
<title>SparkwiseHR Business Card</title>
<link href="https://fonts.googleapis.com/css2?family=Arimo:wght@400;700&display=swap" rel="stylesheet">
<style>
  :root {
    --stage: #dcdcdc;
    --card-white: #ffffff;
    --brand-yellow: #f6b51e;
    --brand-yellow-light: #f7d65a;
    --brand-gold: #f0a818;
    --ink: #111111;
    --mascot-light: #f3e6d3;
    --mascot-shade: #e7d9c6;
    --chip: #3d6fb8;
  }
  * { box-sizing: border-box; margin: 0; padding: 0; }
  html, body {
    width: 1200px; height: 900px; overflow: hidden;
    background: var(--stage);
    font-family: "Arimo", Arial, sans-serif;
  }
  .stage {
    position: relative; width: 1200px; height: 900px;
    display: flex; align-items: center; justify-content: center; gap: 40px;
  }
  .card {
    position: relative; width: 540px; height: 310px;
    border-radius: 22px; overflow: hidden;
    box-shadow: 0 14px 28px rgba(0,0,0,0.18);
  }
  .brand { position: absolute; display: flex; align-items: center; gap: 12px; }
  .brand-mark { border-radius: 50%; background: var(--brand-yellow); flex: none; }
  .brand-name { font-weight: 700; color: var(--ink); letter-spacing: -0.5px; line-height: 1; }
  .brand-tagline { font-weight: 700; color: var(--ink); letter-spacing: 0.2px; margin-top: 4px; }
  .mascot { position: absolute; border-radius: 40% 40% 12px 12px; }

  /* Front */
  .card-front { background: var(--card-white); }
  .card-front .brand { left: 28px; top: 38px; }
  .card-front .brand-mark { width: 62px; height: 62px; }
  .card-front .brand-name { font-size: 38px; }
  .card-front .brand-tagline { font-size: 10.5px; }
  .band {
    position: absolute; left: 0; right: 0; top: 138px; height: 12px;
    background: linear-gradient(90deg, var(--brand-gold), var(--brand-yellow-light));
  }
  .person { position: absolute; left: 24px; top: 164px; }
  .person-name { color: var(--brand-gold); font-weight: 700; font-size: 16px; }
  .person-title { color: var(--ink); font-size: 12px; margin-top: 5px; }
  .contacts { position: absolute; left: 24px; top: 232px; list-style: none; }
  .contacts li {
    display: flex; align-items: center; gap: 6px;
    font-size: 15px; color: var(--ink); line-height: 19px;
  }
  .contacts svg { width: 12px; height: 12px; flex: none; }
  .card-front .mascot {
    right: 40px; bottom: 18px; width: 104px; height: 128px;
    background: linear-gradient(180deg, var(--mascot-light), var(--mascot-shade));
  }

  /* Back */
  .card-back {
    background: linear-gradient(180deg, var(--brand-yellow-light) 0%, var(--brand-yellow) 100%);
  }
  .card-back .brand { left: 34px; top: 52px; }
  .card-back .brand-mark { width: 78px; height: 78px; background: var(--brand-gold); }
  .card-back .brand-name { font-size: 44px; }
  .card-back .brand-tagline { font-size: 11.5px; }
  .social { position: absolute; left: 38px; top: 226px; list-style: none; }
  .social li {
    display: flex; align-items: center; gap: 7px;
    font-size: 16px; color: var(--card-white); line-height: 19px;
  }
  .social .network-chip { width: 13px; height: 13px; border-radius: 2px; background: var(--chip); flex: none; }
  .card-back .mascot {
    right: 30px; bottom: 50px; width: 90px; height: 140px;
    background: linear-gradient(180deg, var(--mascot-light), var(--brand-yellow-light));
  }
</style>
</head>
<body>
<main class="stage">
  <section class="card card-front" aria-label="Card front">
    <div class="brand">
      <span class="brand-mark"></span>
      <div>
        <div class="brand-name">SparkwiseHR</div>
        <div class="brand-tagline">HR PROCESS MANAGEMENT SOLUTIONS</div>
      </div>
    </div>
    <div class="band"></div>
    <div class="person">
      <div class="person-name">Dana Whitfield</div>
      <div class="person-title">Marketing Wizard</div>
    </div>
    <ul class="contacts">
      <li>
        <svg viewBox="0 0 12 12"><path d="M2.5 1 L4.5 1 L5.2 3.5 L4 4.5 Q5 7 7.5 8 L8.5 6.8 L11 7.5 L11 9.5 Q10.5 11 9 11 Q1 10 1 3 Q1 1.5 2.5 1Z" fill="var(--brand-gold)"/></svg>
        555-010-2468
      </li>
      <li>
        <svg viewBox="0 0 12 12"><rect x="0.5" y="2" width="11" height="8" rx="1" fill="var(--brand-gold)"/><path d="M1 2.5 L6 6.5 L11 2.5" stroke="#fff" stroke-width="1" fill="none"/></svg>
        dana@sparkwisehr.com
      </li>
      <li>
        <svg viewBox="0 0 12 12"><circle cx="6" cy="6" r="5" fill="none" stroke="var(--brand-gold)" stroke-width="1.2"/><ellipse cx="6" cy="6" rx="2.2" ry="5" fill="none" stroke="var(--brand-gold)" stroke-width="1"/><path d="M1 6 H11" stroke="var(--brand-gold)" stroke-width="1"/></svg>
        www.sparkwisehr.com
      </li>
    </ul>
    <div class="mascot" role="img" aria-label="Mascot illustration"></div>
  </section>

  <section class="card card-back" aria-label="Card back">
    <div class="brand">
      <span class="brand-mark"></span>
      <div>
        <div class="brand-name">SparkwiseHR</div>
        <div class="brand-tagline">HR PROCESS MANAGEMENT SOLUTIONS</div>
      </div>
    </div>
    <ul class="social">
      <li><span class="network-chip" aria-hidden="true"></span>Gleamrow · sparkwisehrprocess</li>
      <li><span class="network-chip" aria-hidden="true"></span>Brisk Hub · sparkwisehrprocess</li>
      <li><span class="network-chip" aria-hidden="true"></span>Zumbly · sparkwisehrprocess</li>
    </ul>
    <div class="mascot" role="img" aria-label="Mascot illustration"></div>
  </section>
</main>
</body>
</html>
```